Harrowgate Minerals Web Design

Require a Web page design for an international mining and private investment company currently based in Dubai, UAE. I would like to view designs that incorporate our current corporate logo design aimed at communicating global business development/expansion across a diversity of commodities within the mining and investment sectors.

We are a global organisation with global experience and strategy with specific business development focus in Africa, Central and South America.

Target Market(s)

Mining industry, finance, fund raising, brokering, private equity and public stock exchanges.

Industry/Entity Type

Mining

Number of Pages Required

5+ page

Font styles to use
Sans Serif

Colors

Designer to choose colors to be used in the design.

Requirements
Must have
• Corporate logo, description of who we are, what we do, corporate mission, vision & strategy.
Nice to have
• Inclusion of images, photos, interactive maps/graphics and video.

```html
<!DOCTYPE html>
<html lang="en">
<head>
<meta charset="utf-8">
<title>Harrowgate Minerals</title>
<link href="https://fonts.googleapis.com/css2?family=Poppins:wght@500;600;700&family=Barlow:wght@400;500;600&display=swap" rel="stylesheet">
<style>
:root{
  --gold:#c9a35a;
  --gold-light:#e3c98e;
  --gold-dark:#a9823c;
  --ink:#1b1b1b;
  --dark:#151515;
  --dark-2:#222;
  --paper:#ecebe8;
  --text:#333;
  --muted:#8a8a8a;
  --white:#fff;
}
*{box-sizing:border-box;margin:0;padding:0}
html,body{width:1200px;height:3072px;overflow:hidden}
body{position:relative;background:var(--paper);font-family:'Barlow',Arial,sans-serif;color:var(--text)}
.abs{position:absolute}
h1,h2,h3,h4{font-family:'Poppins',Arial,sans-serif}

/* header */
.site-header{left:0;top:0;width:1200px;height:76px;background:#121212}
.brand{left:233px;top:18px;display:flex;align-items:center;gap:10px;font-family:'Poppins',sans-serif;font-weight:600;font-size:22px;color:var(--gold)}
.brand-square{width:30px;height:30px;background:var(--gold)}
.contact-top{left:721px;top:20px;display:flex;gap:10px;align-items:center;color:var(--white);font-size:12px;line-height:16px}
.contact-top b{font-weight:600;font-size:13px}
.icon-circle{width:32px;height:32px;border-radius:50%;background:var(--gold);display:flex;align-items:center;justify-content:center}
.main-nav{left:0;top:76px;width:1200px;height:26px;background:linear-gradient(90deg,#b8924a,#e9d39d 50%,#b8924a)}
.main-nav ul{list-style:none;display:flex;gap:26px;margin-left:233px;line-height:26px;font-size:11px;font-weight:600;text-transform:uppercase;color:#2b2210}

/* hero */
.hero{left:0;top:102px;width:1200px;height:496px;background:linear-gradient(110deg,#1a1612 0%,#2d261d 45%,#5a4a30 75%,#8a7346 100%)}
.hero-title{left:233px;top:158px;width:380px;font-size:23px;line-height:31px;font-weight:600;color:var(--white)}
.btn-gold{background:linear-gradient(#e2c68a,#b99146);color:#2b2210;font-size:11px;font-weight:600;text-transform:uppercase;padding:9px 18px;border-radius:2px}
.hero-btn{left:233px;top:306px}
.hero-dots{left:233px;top:472px;display:flex;gap:5px}
.hero-dots span{width:7px;height:7px;border-radius:50%;border:1px solid var(--gold)}
.hero-dots span.on{background:var(--gold)}

/* who we are */
.about-photo{left:233px;top:649px;width:356px;height:225px;background:linear-gradient(135deg,#1d1d22,#3f3a35 60%,#181818)}
.about-title{left:627px;top:648px;font-size:21px;font-weight:600;color:var(--ink)}
.about-lead{left:627px;top:680px;width:338px;font-size:13px;line-height:17px;color:#333}
.about-body{left:627px;top:735px;width:338px;font-size:11px;line-height:17px;color:#555}
.about-link{left:627px;top:842px;font-size:11px;color:var(--gold);border-bottom:1px solid var(--gold);padding-bottom:3px}
.card-photo{top:911px;width:233px;height:164px}
.card-label{top:1090px;width:233px;text-align:center;font-size:14px;font-weight:500;color:var(--ink)}

/* mission band */
.mission-band{left:0;top:1153px;width:1200px;height:215px;background:#1a1a1a}
.pillar{top:1218px;width:230px;display:flex;gap:14px}
.pillar h3{font-size:13px;font-weight:500;color:var(--white);margin-bottom:10px}
.pillar p{font-size:10.5px;line-height:17px;color:#7d7d7d}

/* projects */
.projects-photo{left:0;top:1368px;width:1200px;height:584px;background:linear-gradient(100deg,#3a2a22 0%,#6b5a48 35%,#a08e74 55%,#6a5238 80%,#3e2c1e 100%)}
.project-panel{left:608px;top:1436px;width:357px;height:498px;background:#f3f1ec}
.project-head{height:70px;background:linear-gradient(#d6b46f,#bd9650);color:var(--white);font-family:'Poppins',sans-serif;font-size:20px;font-weight:600;padding:20px 18px}
.project-item{display:flex;gap:10px;padding:16px 18px;border-bottom:1px solid #ddd8cc;font-size:10.5px;line-height:17px;color:#444}
.project-item b{font-weight:600;color:#222}
.project-item svg{flex:none;margin-top:3px}

/* team */
.team{left:0;top:1952px;width:1200px;height:383px;background:#191919}
.team-title{left:0;top:1992px;width:1200px;text-align:center;font-size:22px;font-weight:600;color:var(--white)}
.member-photo{top:2042px;width:178px;height:180px;background:linear-gradient(#dfe3e6,#9aa3ab)}
.member{top:2232px;width:178px;text-align:center;color:var(--white);font-size:14px;line-height:17px}
.member small{display:block;font-size:10px;color:#888;line-height:13px}
.member-active{top:2222px;height:66px;padding-top:10px;background:var(--gold)}
.member-active small{color:#fff}

/* blog & testimonials */
.section-title{top:2376px;font-size:21px;font-weight:600;color:var(--ink)}
.post-thumb{left:233px;width:135px;height:86px}
.post{left:387px;width:200px}
.post h4{font-family:'Barlow',sans-serif;font-size:13px;font-weight:500;color:#222}
.post .meta{font-size:9.5px;color:#777;margin:3px 0 8px}
.post .meta span{color:var(--gold)}
.post p{font-size:10.5px;line-height:16px;color:#666}
.divider{left:600px;top:2392px;width:1px;height:245px;background:#d2cfc8}
.quote{left:627px;top:2418px;width:338px;display:flex;gap:10px;font-size:10.5px;line-height:17px;color:#666}
.quote-mark{font-family:'Poppins',sans-serif;font-size:30px;line-height:20px;color:#bdb8ad}
.author-avatar{left:657px;top:2574px;width:52px;height:52px;border-radius:50%;background:linear-gradient(#d6b98a,#9a8060);border:3px solid #fff}
.author{left:720px;top:2583px;font-size:13px;color:#333}
.author small{display:block;font-size:10px;color:#888}
.t-dots{left:915px;top:2616px;display:flex;gap:4px}
.t-dots span{width:7px;height:7px;border-radius:50%;border:1px solid var(--gold)}
.t-dots span.on{background:var(--gold)}

/* footer */
.site-footer{left:0;top:2689px;width:1200px;height:383px;background:#1d1d1d}
.footer-scene{left:0;top:2689px;width:1200px;height:128px;background:linear-gradient(#2a2a2a,#1d1d1d)}
.footer-nav{left:0;top:2830px;width:1200px;display:flex;justify-content:center;gap:18px;font-size:10.5px;color:#aaa}
.footer-rule{left:233px;top:2858px;width:732px;height:1px;background:#333}
.office{top:2880px;width:150px;font-size:10.5px;line-height:16px;color:#999}
.office h4{font-family:'Barlow',sans-serif;font-size:13px;font-weight:600;color:var(--white);margin-bottom:6px}
.reach{left:547px;display:flex;gap:10px;font-size:11px;line-height:15px;color:#999}
.reach b{color:var(--white);font-weight:500}
.newsletter{left:795px;top:2880px;width:170px}
.newsletter h4{font-family:'Barlow',sans-serif;font-size:13px;font-weight:600;color:var(--white);margin-bottom:8px}
.newsletter .field{width:170px;height:30px;background:#fff;font-size:9.5px;color:#aaa;padding:9px 10px;margin-bottom:10px}
.newsletter .btn-gold{display:inline-block;font-size:9.5px;padding:6px 14px}
.footer-bottom{left:233px;top:3030px;width:732px;height:1px;background:#333}
.copyright{left:233px;top:3042px;font-size:10px;color:#888}
.social{left:880px;top:3038px;display:flex;gap:6px}
.social span{width:22px;height:22px;background:#5a5a5a}
</style>
</head>
<body>

<header class="site-header abs"></header>
<div class="brand abs"><span class="brand-square"></span>Harrowgate Minerals</div>
<div class="contact-top abs">
  <span class="icon-circle"><svg width="16" height="16" viewBox="0 0 24 24"><path fill="#151515" d="M6.6 10.8a15 15 0 0 0 6.6 6.6l2.2-2.2c.3-.3.7-.4 1-.2 1.1.4 2.3.6 3.6.6.6 0 1 .4 1 1V20c0 .6-.4 1-1 1A17 17 0 0 1 3 4c0-.6.4-1 1-1h3.5c.6 0 1 .4 1 1 0 1.3.2 2.5.6 3.6.1.3 0 .7-.2 1z"/></svg></span>
  <div>Have a question? call us today<br><b>+224 600 118 204 &nbsp;|&nbsp; +61 400 552 716</b></div>
</div>
<nav class="main-nav abs"><ul><li>Executive Summary</li><li>Team &amp; Experience</li><li>Commercial</li><li>Business Model</li><li>Strategy</li><li>Contact</li></ul></nav>

<section class="hero abs" role="img" aria-label="Photo of an excavator bucket loading ore onto a mining haul truck"></section>
<h1 class="hero-title abs">A platform for execution of global mining projects with an initial focus on South America, Central America &amp; Africa.</h1>
<span class="hero-btn btn-gold abs">Get Started</span>
<div class="hero-dots abs"><span class="on"></span><span></span><span></span></div>

<div class="about-photo abs" role="img" aria-label="Photo of mining engineers in hard hats inside an underground tunnel"></div>
<h2 class="about-title abs">Who We Are</h2>
<p class="about-lead abs">Strong industry connections &amp; networks in Africa, South America &amp; Australia.</p>
<p class="about-body abs">Newly formed company to create a platform for execution of global mining projects with an initial focus on South America, Central America &amp; Africa. Strong executive &amp; management team with A to Z in all facets of mining, finance &amp; operations. Properly capitalized to execute its mandate.</p>
<span class="about-link abs">Learn More About Us &rarr;</span>

<div class="card-photo abs" style="left:233px;background:linear-gradient(135deg,#c9b8a6,#7a8a5a 55%,#3c3a30)" role="img" aria-label="Photo of hands together holding a young green seedling"></div>
<div class="card-photo abs" style="left:483px;background:linear-gradient(135deg,#e6ddd0,#b9a58a 50%,#6d6155)" role="img" aria-label="Photo of smiling investors seated at a meeting table"></div>
<div class="card-photo abs" style="left:733px;background:linear-gradient(135deg,#0f1b3a,#23407a 55%,#5b77b8)" role="img" aria-label="Photo of a hand touching a glowing digital world map"></div>
<div class="card-label abs" style="left:233px">Social Responsibility</div>
<div class="card-label abs" style="left:483px">Investors</div>
<div class="card-label abs" style="left:733px">Contact Us</div>

<section class="mission-band abs"></section>
<div class="pillar abs" style="left:233px">
  <svg width="28" height="28" viewBox="0 0 28 28" fill="none" stroke="#c9a35a" stroke-width="1.8"><circle cx="13" cy="15" r="10"/><circle cx="13" cy="15" r="5.5"/><circle cx="13" cy="15" r="1.5" fill="#c9a35a"/><path d="M13 15 25 3M21 3h4v4"/></svg>
  <div><h3>Our Mission</h3><p>Class aptent taciti sociosqu aded nostra per inceptos aeos mauris ut aliquam massa nisl quis neques suspendisse in orci enim.</p></div>
</div>
<div class="pillar abs" style="left:483px">
  <svg width="28" height="28" viewBox="0 0 28 28" fill="none" stroke="#c9a35a" stroke-width="1.8"><path d="M2 14s5-8 12-8 12 8 12 8-5 8-12 8S2 14 2 14z"/><circle cx="14" cy="14" r="4"/></svg>
  <div><h3>Our Vision</h3><p>Class aptent taciti sociosqu aded nostra per inceptos aeos mauris ut aliquam massa nisl quis neques suspendisse in orci enim.</p></div>
</div>
<div class="pillar abs" style="left:733px">
  <svg width="28" height="28" viewBox="0 0 28 28" fill="none" stroke="#c9a35a" stroke-width="1.8"><path d="M4 24h20M8 24l2-8-4-3 8-9 6 5v15"/></svg>
  <div><h3>Our Strategy</h3><p>Class aptent taciti sociosqu aded nostra per inceptos aeos mauris ut aliquam massa nisl quis neques suspendisse in orci enim.</p></div>
</div>

<section class="projects-photo abs" role="img" aria-label="Photo of an engineer in a hard hat on red steel stairs overlooking an open-pit mine"></section>
<div class="project-panel abs">
  <div class="project-head">Project Experience</div>
  <div class="project-item"><svg width="14" height="14" viewBox="0 0 14 14" fill="none" stroke="#c9a35a" stroke-width="1.6"><path d="M2 12 9 5M5 2c3 0 6 2 7 5"/></svg><p>Exploration experts in <b>Brazil, Burkina Faso, Cote d'Ivoire, Colombia, Chile, Ghana, Guinea, Gabon, Togo, Mali, Niger, Nigeria, Peru, Saudi Arabia</b> &amp; more recently the copper belt in <b>Zambia.</b></p></div>
  <div class="project-item"><svg width="14" height="14" viewBox="0 0 14 14" fill="none" stroke="#c9a35a" stroke-width="1.6"><path d="M2 12 9 5M5 2c3 0 6 2 7 5"/></svg><p><b>Kestrel Ridge Mine</b> - an underground polymetallic (Zinc, lead, gold &amp; copper) mine located on Tasmania's west coast. Australia. 2017 production target: over 65,000 tonnes of zinc in zinc concentrate over 18,000 tonnes of lead.</p></div>
  <div class="project-item"><svg width="14" height="14" viewBox="0 0 14 14" fill="none" stroke="#c9a35a" stroke-width="1.6"><path d="M2 12 9 5M5 2c3 0 6 2 7 5"/></svg><p><b>Alto Verde mine</b> - a long-life open pit copper mine located in the Apurimac region of Peru. Target production rate - over 420K tonnes copper per year.</p></div>
  <div class="project-item" style="border:0"><svg width="14" height="14" viewBox="0 0 14 14" fill="none" stroke="#c9a35a" stroke-width="1.6"><path d="M2 12 9 5M5 2c3 0 6 2 7 5"/></svg><p>The <b>Serra Clara</b> facility in South East Brazil with an installed capacity to produce approximately 8 million tons of iron ore annually from the Pedra Alta &amp; Rio Seco mines belonging to Norte Ferro Brazil.</p></div>
</div>

<section class="team abs"></section>
<h2 class="team-title abs">Executive Team</h2>
<div class="member-photo abs" style="left:233px" role="img" aria-label="Portrait photo of the chairman"></div>
<div class="member-photo abs" style="left:420px" role="img" aria-label="Portrait photo of the CEO"></div>
<div class="member-photo abs" style="left:602px" role="img" aria-label="Portrait photo of the CFO"></div>
<div class="member-photo abs" style="left:787px" role="img" aria-label="Portrait photo of the technical director"></div>
<div class="member abs" style="left:233px">Graham Whitlow<small>Chairman</small></div>
<div class="member abs" style="left:420px">Daniel Marsh<small>CEO</small></div>
<div class="member member-active abs" style="left:602px">Owen Pellham<small>CFO</small></div>
<div class="member abs" style="left:787px">Rafael Souza Lima<small>Technical Director and<br>Country Manager (Brazil)</small></div>

<h2 class="section-title abs" style="left:233px">From the Blog</h2>
<div class="post-thumb abs" style="top:2427px;background:linear-gradient(135deg,#22252b,#4a4640)" role="img" aria-label="Photo of miners in an underground tunnel"></div>
<div class="post abs" style="top:2422px"><h4>Lorem Ipsum charsets layouts</h4><div class="meta">By <span>Mark Ellery</span> | 03 May 2018</div><p>Class aptent taciti sociosqu ad litora torquent per conubia himenaeos. Mauris in erat justo.</p></div>
<div class="post-thumb abs" style="top:2540px;background:linear-gradient(135deg,#9aa4ad,#c9a35a 60%,#6c5f4d)" role="img" aria-label="Photo of yellow haul trucks at a mine site"></div>
<div class="post abs" style="top:2535px"><h4>Lorem Ipsum charsets layouts</h4><div class="meta">By <span>Mark Ellery</span> | 03 May 2018</div><p>Class aptent taciti sociosqu ad litora torquent per conubia himenaeos. Mauris in erat justo.</p></div>
<div class="divider abs"></div>

<h2 class="section-title abs" style="left:627px">Testimonials</h2>
<div class="quote abs"><span class="quote-mark">&ldquo;</span><p>Class aptent taciti sociosqu ad litora torquent per conubia nostra, per inceptos himenaeos. Mauris in condimentum sit amet a augue. Sed non neque elit. Sed ut imperdiet nisi. Proin condimentum fermentum nunc. Etiam pharetra, erat sed fermentum feugiat, velit mauris egestas quam, ut aliquam massa nisl quis neque. Suspendisse in orci enim. Mauris in condimentum sit amet a augue. Sed non fermentum feugiat, velit mauris egestas quam, neque elit.</p></div>
<div class="author-avatar abs" role="img" aria-label="Portrait photo of the client"></div>
<div class="author abs">~ Peter Hale<small>Lorem ipsum dolor</small></div>
<div class="t-dots abs"><span class="on"></span><span></span><span></span><span></span><span></span></div>

<footer class="site-footer abs"></footer>
<div class="footer-scene abs" role="img" aria-label="Faint illustration of mining vehicles and workers along the top of the footer"></div>
<div class="footer-nav abs"><span>Executive Summary</span><span>Team &amp; Experience</span><span>Commercial</span><span>Business Model</span><span>Strategy</span><span>Contact</span></div>
<div class="footer-rule abs"></div>
<div class="office abs" style="left:233px"><h4>Dubai, UAE</h4>Suite 210, Tower 3,<br>Marina Walk,<br>Harbour Quarter,<br>Business Bay,<br>Dubai, UAE.</div>
<div class="office abs" style="left:383px"><h4>Guinea, West Africa</h4>Rue des Palmiers,<br>Immeuble 12,<br>Conakry,<br>BP: 4410</div>
<div class="reach abs" style="top:2880px"><span class="icon-circle"><svg width="15" height="15" viewBox="0 0 24 24"><path fill="#151515" d="M6.6 10.8a15 15 0 0 0 6.6 6.6l2.2-2.2c.3-.3.7-.4 1-.2 1.1.4 2.3.6 3.6.6.6 0 1 .4 1 1V20c0 .6-.4 1-1 1A17 17 0 0 1 3 4c0-.6.4-1 1-1h3.5c.6 0 1 .4 1 1 0 1.3.2 2.5.6 3.6.1.3 0 .7-.2 1z"/></svg></span><div>Call Us :<br><b>+224 600 118 204<br>+61 400 552 716</b></div></div>
<div class="reach abs" style="top:2938px"><span class="icon-circle"><svg width="15" height="15" viewBox="0 0 24 24" fill="none" stroke="#151515" stroke-width="2.2"><rect x="3" y="5" width="18" height="14"/><path d="m3 6 9 7 9-7"/></svg></span><div>Email Us :<br><b>info@harrowgateminerals.com</b></div></div>
<div class="newsletter abs"><h4>Subscribe Newsletter</h4><div class="field">Email Address</div><span class="btn-gold">Subscribe</span></div>
<div class="footer-bottom abs"></div>
<div class="copyright abs">&copy; 2018 Harrowgate Minerals. All Rights Reserved</div>
<div class="social abs"><span></span><span></span><span></span></div>

</body>
</html>
```